Business Design for Printed Shipping Tape

We need a company logo design to be printed on packaging natural color WAT tape for shipping boxes. www.brightmeadowkelp.com
The tape is 3" wide. Repeat pattern every 10 inches.
Would like our website vertical at one end side and "The Future of Nutrition" on the opposite end.

Industry/Entity Type

Health, Nutrition

Font styles to use
Sans Serif

Requirements
Must have
• Company Logo (attached) website and text "The Future of Nutrition"
Nice to have
• Tape is Natural Color.

```html
<!DOCTYPE html>
<html lang="en">
<head>
<meta charset="utf-8">
<title>Bright Meadow Kelp – Shipping Tape</title>
<link rel="stylesheet" href="https://fonts.googleapis.com/css2?family=Poppins:ital,wght@0,500;0,700;1,900&display=swap">
<style>
  :root {
    --backdrop: #3b3b3d;
    --teal: #25a894;
    --paper: #ffffff;
    --ink: #333333;
  }
  * { margin: 0; padding: 0; box-sizing: border-box; }
  html, body {
    width: 1200px; height: 503px; overflow: hidden;
    background: var(--backdrop);
    font-family: "Poppins", sans-serif;
  }
  .canvas { position: relative; width: 1200px; height: 503px; }
  .tape {
    position: absolute; left: 129px; top: 110px;
    width: 942px; height: 283px;
    background: var(--teal);
    overflow: hidden;
  }
  .tape__panel { position: absolute; left: 0; top: 0; }
  .brand {
    position: absolute; left: 66px; top: 62px; width: 302px;
    text-align: center; color: var(--ink);
  }
  .brand__dot {
    display: block; width: 46px; height: 46px; margin: 0 auto 6px;
    border-radius: 50%; background: var(--teal);
  }
  .brand__name {
    font-weight: 700; font-size: 38px; line-height: 49px;
    letter-spacing: 0; text-transform: uppercase;
    white-space: nowrap;
  }
  .headline {
    position: absolute; left: 430px; top: 56px;
    color: var(--paper);
    font-weight: 900; font-style: italic;
    font-size: 78px; line-height: 56px;
    letter-spacing: -2.5px; text-transform: uppercase;
    white-space: nowrap;
  }
  .headline span { display: block; }
  .headline .line-1 { padding-left: 16px; }
  .headline .line-2 { padding-left: 12px; }
  .website {
    position: absolute; left: 810px; top: 133px;
    width: 190px; height: 14px;
    transform: rotate(-90deg);
    transform-origin: center;
    color: var(--paper);
    font-weight: 500; font-size: 12px; line-height: 14px;
    text-align: center; white-space: nowrap;
  }
</style>
</head>
<body>
  <div class="canvas">
    <div class="tape">
      <svg class="tape__panel" width="942" height="283" viewBox="0 0 942 283" aria-hidden="true">
        <polygon points="51,0 430,0 379,283 0,283" fill="var(--paper)"/>
      </svg>

      <div class="brand">
        <span class="brand__dot" aria-hidden="true"></span>
        <p class="brand__name">Bright<br>Meadow Kelp</p>
      </div>

      <h1 class="headline">
        <span class="line-1">The</span>
        <span class="line-2">Futureof</span>
        <span class="line-3">Nutrition</span>
      </h1>

      <p class="website">www.brightmeadowkelp.com</p>
    </div>
  </div>
</body>
</html>
```